IV Bag Graphic for IV Therapy Bar

Hello we are offering an IV Therapy Bar to our medical practice. We already have a logo would like a cool design label for the IV bag. We will utilize this label for social media advertising, a sticker for the saline bag and marketing material. Woukd like something unique, sharp, bold and professional. We signed up for the Social Media package so the design will need to hold and be creative.

Target Market(s)

25-35 yrs old

Requirements
Must have
• Bellwood Clinical Research name and logo- Clear inference it is IV therapy
Nice to have
• Innovation- Lines to write Name - Also please give examples of the different IV therapies (Myers cocktail) etc (screenshot example of therapies is attached)
Should not have
• In the attached examples the packaging and label are black, in open.

```html
<!DOCTYPE html>
<html lang="en">
<head>
<meta charset="UTF-8">
<title>Wellness Drip Labels – Bellwood Clinical Research</title>
<link rel="stylesheet" href="https://fonts.googleapis.com/css2?family=Bebas+Neue&family=Quicksand:wght@400;500;600&display=swap">
<style>
  :root {
    --page: #ffffff;
    --label: #000000;
    --ink: #ffffff;
    --magenta: #ee36c9;
    --mint: #19e48f;
    --aqua: #06d2e8;
  }
  * { margin: 0; padding: 0; box-sizing: border-box; }
  html, body {
    width: 1200px;
    height: 873px;
    overflow: hidden;
    background: var(--page);
  }
  .drip-range {
    position: relative;
    width: 1200px;
    height: 873px;
  }
  .drip-label {
    position: absolute;
    top: 224px;
    width: 236px;
    height: 409px;
    background: var(--label);
    border-radius: 6px;
    color: var(--ink);
    font-family: "Quicksand", sans-serif;
  }
  .drip-label--weight { left: 135px; --accent: var(--magenta); }
  .drip-label--immune { left: 474px; --accent: var(--mint); }
  .drip-label--relax  { left: 804px; --accent: var(--aqua); }

  .icon-tab {
    position: absolute;
    top: 0;
    left: 63px;
    width: 107px;
    height: 67px;
    background: var(--accent);
    border-radius: 0 0 6px 6px;
  }
  .drip-title {
    position: absolute;
    top: 84px;
    left: 0;
    width: 100%;
    text-align: center;
    font-family: "Bebas Neue", sans-serif;
    font-size: 44px;
    line-height: 1;
    letter-spacing: 0.5px;
  }
  .drip-label--immune .drip-title { font-size: 43px; }
  .title-rule {
    position: absolute;
    top: 136px;
    left: 22px;
    width: 188px;
    height: 2px;
    background: var(--ink);
  }
  .drip-subtitle {
    position: absolute;
    top: 146px;
    left: 0;
    width: 100%;
    text-align: center;
    font-size: 23px;
    font-weight: 500;
    letter-spacing: 0.3px;
  }
  .ingredient-list {
    position: absolute;
    top: 212px;
    left: 30px;
    list-style: none;
  }
  .ingredient-list li {
    position: relative;
    padding-left: 12px;
    font-size: 11.5px;
    font-weight: 500;
    letter-spacing: 1px;
    line-height: 20.7px;
  }
  .ingredient-list li::before {
    content: "";
    position: absolute;
    left: 0;
    top: 7px;
    width: 5.5px;
    height: 5.5px;
    border-radius: 50%;
    background: var(--ink);
  }
  .volume {
    position: absolute;
    left: 30px;
    font-size: 10.5px;
    font-weight: 500;
  }
  .drip-label--weight .volume { top: 378px; }
  .drip-label--immune .volume,
  .drip-label--relax .volume { top: 358px; }
  .brand-mark {
    position: absolute;
    right: 12px;
    bottom: 12px;
    width: 96px;
    text-align: center;
    font-size: 10px;
    font-weight: 600;
    line-height: 1.25;
    letter-spacing: 0.3px;
  }
  .brand-dot {
    display: block;
    width: 38px;
    height: 38px;
    margin: 0 auto 6px;
    border-radius: 50%;
    background: var(--ink);
  }
</style>
</head>
<body>
<main class="drip-range">

  <section class="drip-label drip-label--weight">
    <div class="icon-tab" role="img" aria-label="Icon of a bathroom scale with footprints and a downward arrow"></div>
    <h2 class="drip-title">Weight Loss</h2>
    <div class="title-rule"></div>
    <p class="drip-subtitle">WELLNESS DRIP</p>
    <ul class="ingredient-list">
      <li>B-COMPLEX VITAMIN</li>
      <li>VITAMIN B12</li>
      <li>L-ARGININE</li>
      <li>L-CARNITINE</li>
      <li>L GLUTAMINE</li>
      <li>TAURINE</li>
      <li>MIC</li>
    </ul>
    <p class="volume">1000 ML</p>
    <p class="brand-mark"><span class="brand-dot"></span>BELLWOOD CLINICAL RESEARCH</p>
  </section>

  <section class="drip-label drip-label--immune">
    <div class="icon-tab" role="img" aria-label="Icon of a shield with a medical cross warding off germs"></div>
    <h2 class="drip-title">Immune Boost</h2>
    <div class="title-rule"></div>
    <p class="drip-subtitle">WELLNESS DRIP</p>
    <ul class="ingredient-list">
      <li>VITAMIN B-COMPLEX</li>
      <li>VITAMIN B12</li>
      <li>VITAMIN C</li>
      <li>GLUTATHIONE</li>
      <li>ZINC</li>
    </ul>
    <p class="volume">1000 ML</p>
    <p class="brand-mark"><span class="brand-dot"></span>BELLWOOD CLINICAL RESEARCH</p>
  </section>

  <section class="drip-label drip-label--relax">
    <div class="icon-tab" role="img" aria-label="Icon of a head in profile with a calm starburst in the mind"></div>
    <h2 class="drip-title">Relaxation</h2>
    <div class="title-rule"></div>
    <p class="drip-subtitle">WELLNESS DRIP</p>
    <ul class="ingredient-list">
      <li>NORMAL SALIN</li>
      <li>MAGNESIUM</li>
      <li>TAURINE</li>
      <li>MULTIVITAMIN</li>
    </ul>
    <p class="volume">1000 ML</p>
    <p class="brand-mark"><span class="brand-dot"></span>BELLWOOD CLINICAL RESEARCH</p>
  </section>

</main>
</body>
</html>
```